Verdant Orchard - Stationery Design Project

We need a stationary for our business. We grow roots and fruits in Central and South America, we import and distribute in FL, USA. We do fresh and frozen products.

Target Market(s)

Small and big supermarkets, wholesalers, traders, distributors, etc

Industry/Entity Type

Business

```html
<!DOCTYPE html>
<html lang="en">
<head>
<meta charset="utf-8">
<title>Verdant Orchard Group – Stationery</title>
<link rel="stylesheet" href="https://fonts.googleapis.com/css2?family=Montserrat:wght@300;400;500;600&display=swap">
<style>
:root{
  --bg-top:#e9edef;
  --bg-bottom:#d6dde0;
  --sheet:#ffffff;
  --sheet-back:#f1f1f1;
  --brand-orange:#e8830f;
  --brand-green:#5a6b2e;
  --rule:#8d8d8d;
  --ink:#3a3a3a;
  --ink-dark:#1e1e1e;
}
*{margin:0;padding:0;box-sizing:border-box}
html,body{width:1200px;height:927px;overflow:hidden}
body{
  position:relative;
  background:linear-gradient(180deg,var(--bg-top),var(--bg-bottom));
  font-family:"Montserrat",sans-serif;
  color:var(--ink);
}
.sheet{
  position:absolute;top:45px;width:512px;height:696px;
  border-radius:12px;
  box-shadow:0 1px 4px rgba(0,0,0,.25);
}
.sheet--front{left:43px;background:var(--sheet)}
.sheet--back{left:635px;background:var(--sheet-back)}

.brand-name{
  position:absolute;left:0;right:0;text-align:center;
  font-weight:500;color:var(--brand-orange);
  letter-spacing:.5px;white-space:nowrap;
}
.sheet--front .brand-name{top:44px;font-size:22px}
.sheet--back .brand-name{top:600px;font-size:22px}

.header-rule{position:absolute;left:45px;top:100px;width:430px;height:2px;background:var(--rule)}
.web{
  position:absolute;left:0;right:0;top:105px;text-align:center;
  font-size:9.5px;font-weight:600;letter-spacing:1.3px;color:var(--ink-dark);
}
.web span{color:var(--brand-orange)}

.watermark{
  position:absolute;left:0;right:0;top:338px;text-align:center;
  font-size:44px;font-weight:500;color:var(--brand-orange);opacity:.1;
  white-space:nowrap;pointer-events:none;
}

.letter-body{position:absolute;left:42px;top:140px;width:430px}
.letter-body p{
  font-size:10.6px;line-height:18px;font-weight:400;
  text-align:justify;hyphens:auto;margin-bottom:18px;
}
.signature{position:absolute;left:382px;top:586px}
.signature .name{font-size:13.5px;font-weight:400;color:var(--ink-dark)}
.signature .title{font-size:8.5px;margin-top:6px}

.contact-bar{
  position:absolute;left:23px;right:36px;top:677px;
  display:flex;justify-content:space-between;
  font-size:9.5px;font-weight:600;color:var(--ink-dark);
}

.features{
  position:absolute;left:34px;top:806px;list-style:none;
  font-size:24px;font-weight:400;color:#111;line-height:34px;letter-spacing:.3px;
}
</style>
</head>
<body>

<section class="sheet sheet--front" aria-label="Letterhead">
  <div class="brand-name">VERDANT ORCHARD GROUP</div>
  <div class="header-rule"></div>
  <div class="web">www.<span>verdantorchardgroup</span>.com</div>
  <div class="watermark">VERDANT ORCHARD</div>

  <div class="letter-body">
    <p>Lorem ipsum dolor sit amet, consectetur adipiscing elit. Donec orci purus, luctus vitae dignissim eu, iaculis sed purus. Vivamus faucibus, ipsum nec aliquet viverra, leo mauris condimentum ligula, sit amet sagittis enim ligula quis arcu. Nam egestas tortor id nisi porttitor mattis. In tortor ante, ultricies in suscipit a, tempus non massa. Vivamus et auctor mi. Fusce vel massa nulla. Phasellus nec eros mauris, et scelerisque orci. Donec malesuada orci vitae nulla accumsan porta a id massa.</p>
    <p>Quisque accumsan iaculis magna sit amet fringilla. Maecenas consequat, magna eget tincidunt semper, odio nibh rutrum mi, id feugiat ante nisi eu risus. Vestibulum nunc orci, rhoncus a placerat in, ultricies in mi. Cras mattis varius eros, vel fringilla nisi suscipit eget. Quisque scelerisque sagittis nulla at porttitor. Mauris a justo et tellus interdum tristique. Sed id augue vitae urna euismod commodo aliquet a quam. Pellentesque arcu velit, cursus et malesuada ut, consequat et diam. Nullam erat sem, rhoncus id ullamcorper vitae, rhoncus et arcu. In ultricies ultricies nulla,</p>
    <p>Kut rutrum nisi iaculis at. Donec eu magna a metus ornare faucibus. Fusce aliquet faucibus ultricies. Morbi semper, est id tincidunt gravida, sem arcu adipiscing lacus, ac bibendum nulla leo eu purus. Quisque nec diam sed risus consectetur a ccumsan quis quis nibh. Vestibulum id purus lorem. Donec eu magna a metus ornare faucibus. Fusce aliquet faucibus ultricies. Morbi semper, est id tincidunt gravida, sem arcu adipiscing lacus, ac bibendum nulla leo eu purus. Quisque nec diam sed risus consectetur a ccumsan quis quis nibh. Vestibulum id purus lorem.</p>
  </div>

  <div class="signature">
    <div class="name">Daniel Reyes</div>
    <div class="title">Co-Founder &amp; CEO</div>
  </div>

  <div class="contact-bar">
    <span>Ph: 555.201.4830</span>
    <span>Fax: 555.201.4831</span>
    <span>Toll Free: 800.555.0193</span>
  </div>
</section>

<section class="sheet sheet--back" aria-label="Letterhead reverse">
  <div class="brand-name">VERDANT ORCHARD GROUP</div>
</section>

<ul class="features">
  <li>- PRINT READY &amp; EDITABLE FILES</li>
  <li>- PSD, JPG, TIFF, PNG, AI, EPS&nbsp; FILE FORMATS</li>
  <li>- UNLIMITED REVISIONS ARE MOST WELCOME</li>
</ul>

</body>
</html>
```